ServLoom Website Homepage Design

Please provide your idea of homepage for a hosting company. This project is for DESIGN only, no coding.

It must use/combine colors used in logo, clean, modern look.

Homepage must consist of at least 4 sections (example: testimonials, services, and so on. not necesarily all of them). We would like the navigation to be horizontal, but not mandatory.

You can include a preview of services page (optional, not a must).

Number of Pages Required

1 page

Font styles to use
Sans Serif

```html
<!DOCTYPE html>
<html lang="en">
<head>
<meta charset="utf-8">
<title>ServLoom — Premium Hosting</title>
<link href="https://fonts.googleapis.com/css2?family=Merriweather+Sans:wght@400;700;800&family=Lato:wght@400;700&display=swap" rel="stylesheet">
<style>
:root{
  --blue:#1593e6;
  --blue-deep:#1b3fb3;
  --navy:#1f2a44;
  --text:#3d4454;
  --muted:#7a8292;
  --orange:#ee6c14;
  --yellow:#fbb42a;
  --red:#e53935;
  --tint:#e7f3fc;
  --white:#ffffff;
  --line:#d3d9e2;
}
*{box-sizing:border-box;margin:0;padding:0}
html,body{width:1200px;height:4963px;overflow:hidden;background:var(--white)}
body{position:relative;font-family:"Lato",sans-serif;color:var(--text)}
.abs{position:absolute}
h1,h2,h3,h4,.head{font-family:"Merriweather Sans",sans-serif}
.brand{font-family:"Merriweather Sans",sans-serif;font-weight:800;letter-spacing:.5px;color:var(--blue)}
.btn{position:absolute;display:flex;align-items:center;justify-content:center;border-radius:20px;font-family:"Merriweather Sans",sans-serif;font-size:11px;font-weight:700}
.btn-solid{background:var(--blue);color:var(--white)}
.btn-line{border:2px solid var(--blue);color:var(--blue);background:var(--white)}
.blob{position:absolute;border-radius:50%;background:var(--tint)}
.sec-title{position:absolute;font-size:22px;font-weight:800;color:var(--navy);white-space:nowrap}
.sec-title em{font-style:normal;color:var(--blue)}
.rule{position:absolute;height:2px;background:var(--orange)}
.sec-sub{position:absolute;left:0;width:1200px;text-align:center;font-size:11px;color:var(--text)}
.center{left:0;width:1200px;text-align:center}

/* header */
.nav a{position:absolute;top:28px;font-size:12px;color:var(--white);text-decoration:none}
.hero-copy p{font-size:12.5px;line-height:19px;color:var(--text)}

/* domain search */
.search{left:368px;top:609px;width:460px;height:42px;background:var(--white);box-shadow:0 3px 14px rgba(30,60,110,.13);border-radius:3px}
.search .hint{position:absolute;left:32px;top:14px;font-size:10px;color:#a6adb9}
.search .tld{position:absolute;left:295px;top:12px;font-size:13px;color:var(--navy)}
.search .divider{position:absolute;left:283px;top:6px;width:1px;height:30px;background:var(--line)}
.search .go{position:absolute;left:366px;top:0;width:94px;height:42px;background:var(--blue);color:#fff;border-radius:3px;display:flex;align-items:center;justify-content:center;font-size:11px;font-weight:700;box-shadow:0 4px 10px rgba(21,147,230,.35)}
.partner{position:absolute;top:722px;display:flex;align-items:center;gap:8px;font-family:"Merriweather Sans",sans-serif;font-weight:700;font-size:19px;color:#4a5366;transform:translateX(-50%)}
.partner i{display:block;width:14px;height:14px;background:#4a5366}

/* why cards */
.why{position:absolute;top:973px;width:231px;height:217px;background:var(--white);box-shadow:0 4px 18px rgba(30,60,110,.12);padding:20px 20px}
.why h3{font-size:14px;font-weight:700;color:var(--navy)}
.why svg{position:absolute;left:20px;top:58px}
.why .dash{position:absolute;left:20px;top:108px;width:20px;height:2px;background:var(--navy)}
.why p{position:absolute;left:20px;top:122px;width:190px;font-size:11.5px;line-height:19px}
.why.featured{background:linear-gradient(160deg,#1aa3f0,#1583de);color:#fff}
.why.featured h3{color:#fff}
.why.featured .dash{background:#fff}

/* features band */
.band{left:0;top:1285px;width:1200px;height:414px;background:linear-gradient(180deg,#1792e6 0%,#1d59c8 60%,#1c3fb3 100%)}
.tile{position:absolute;width:121px;height:119px;background:var(--white);border-top:3px solid var(--blue);text-align:center}
.tile svg{position:absolute;left:40px;top:14px}
.tile span{position:absolute;left:0;width:121px;bottom:22px;font-size:11.5px;font-weight:700;color:var(--navy)}

/* pricing */
.plan{position:absolute;top:1928px;width:253px;height:392px;background:var(--white);box-shadow:0 4px 20px rgba(30,60,110,.12);text-align:center}
.plan .cap{height:42px;color:#fff;font-size:11px;font-weight:700;font-family:"Merriweather Sans",sans-serif;display:flex;align-items:center;justify-content:center;letter-spacing:.4px}
.plan .price{position:absolute;left:0;width:253px;top:66px;font-family:"Merriweather Sans",sans-serif;font-weight:800;font-size:42px;color:var(--navy)}
.plan .tier{position:absolute;left:0;width:253px;top:130px;font-size:14px;color:var(--text)}
.plan ul{position:absolute;left:72px;top:164px;list-style:none;text-align:left}
.plan li{height:25px;font-size:10.5px;color:var(--text);display:flex;align-items:center;gap:7px}
.plan li b{display:block;width:9px;height:9px;border-radius:50%;background:var(--blue)}
.plan li b.no{background:var(--red)}
.plan .buy{position:absolute;left:84px;top:326px;width:85px;height:28px;border-radius:14px;color:#fff;font-size:10px;font-weight:700;display:flex;align-items:center;justify-content:center}

/* guarantee */
.guarantee{left:0;top:2516px;width:1200px;height:235px;background:linear-gradient(100deg,#2a36a8 0%,#3146bd 50%,#2d3fb2 100%)}
.perk{position:absolute;font-size:12px;color:#fff;display:flex;align-items:center;gap:8px}
.perk i{display:block;width:9px;height:9px;border-radius:50%;background:#1ab3f0}

/* testimonials */
.ring{position:absolute;border-radius:50%;border:1px solid #eef1f5;box-shadow:0 0 40px rgba(30,60,110,.05), inset 0 0 30px rgba(30,60,110,.04)}
.avatar{position:absolute;width:54px;height:54px;background:linear-gradient(145deg,#b9c2cf,#7d8899);box-shadow:0 3px 10px rgba(0,0,0,.15)}
.quote-card{left:383px;top:3056px;width:430px;height:171px;border:2px solid var(--blue);border-radius:8px}

/* blog */
.post{position:absolute;top:3601px;width:253px}
.post .thumb{height:218px}
.post time{display:block;margin-top:18px;font-size:10px;color:var(--muted)}
.post h4{margin-top:10px;font-size:13.5px;line-height:22px;color:var(--blue);font-weight:700}
.post p{margin-top:7px;font-size:11.5px;line-height:19px}
.post a{display:block;margin-top:8px;font-size:10px;font-weight:700;color:var(--blue);text-decoration:none}

/* contact */
.form{left:318px;top:4213px;width:563px;height:384px;background:var(--white);box-shadow:0 6px 28px rgba(30,60,110,.14)}
.field{position:absolute;height:37px;border:1px solid var(--line)}
.field label{position:absolute;left:18px;top:-7px;background:#fff;padding:0 5px;font-size:9px;color:var(--navy);letter-spacing:.2px}

/* footer */
.foot h4{position:absolute;font-size:12px;font-weight:700;color:#fff}
.foot a,.foot span{position:absolute;font-size:11px;color:#fff;text-decoration:none;display:flex;align-items:center;gap:7px}
.foot a i{display:block;width:8px;height:8px;border-radius:50%;background:#fff}
</style>
</head>
<body>

<!-- HERO -->
<header>
  <div class="blob" style="left:-150px;top:395px;width:300px;height:300px"></div>
  <svg class="abs" style="left:491px;top:0" width="709" height="428" role="img" aria-label="Photo of a presenter speaking to a seated team in a brick-walled office">
    <defs>
      <linearGradient id="heroPhoto" x1="0" y1="0" x2="1" y2="1">
        <stop offset="0" stop-color="#c7b49c"/>
        <stop offset=".45" stop-color="#8d7f72"/>
        <stop offset="1" stop-color="#4c5868"/>
      </linearGradient>
    </defs>
    <path d="M40 0 H709 V428 H200 Q160 428 145 398 L12 120 Q0 92 10 62 Z" fill="url(#heroPhoto)"/>
  </svg>
  <div class="abs brand" style="left:189px;top:27px;font-size:16px">SERVLOOM</div>
  <nav class="nav">
    <a style="left:615px">Home</a>
    <a style="left:674px">Domain</a>
    <a style="left:747px">Blog</a>
    <a style="left:800px">Plans</a>
    <a style="left:855px">Contact</a>
  </nav>
  <div class="btn btn-solid" style="left:927px;top:19px;width:83px;height:31px">Login</div>
  <div class="hero-copy">
    <h1 class="abs" style="left:189px;top:134px;font-size:34px;line-height:47px;font-weight:800;color:var(--blue)">Best Premium<br>Hosting Services</h1>
    <p class="abs" style="left:189px;top:243px;width:290px">Lorem ipsum dolor sit amet, consectetur adipiscing elit. In purus urna, maximus eu consequat non, sollicitudin nec nisi. Cras non</p>
  </div>
  <div class="btn btn-solid" style="left:189px;top:318px;width:141px;height:40px">View Plans</div>
  <div class="btn btn-line" style="left:351px;top:318px;width:140px;height:40px">Our Services</div>
</header>

<!-- DOMAIN SEARCH -->
<section>
  <h2 class="sec-title" style="left:354px;top:523px">Start Your Journey with Your <em>Perfect Domain.</em></h2>
  <div class="rule" style="left:354px;top:564px;width:174px"></div>
  <div class="abs search">
    <span class="hint">Enter Your Domain name here</span>
    <span class="divider"></span>
    <span class="tld">.com ⌄</span>
    <span class="go">Search</span>
  </div>
  <div class="partner" style="left:289px"><i></i>Paynest</div>
  <div class="partner" style="left:522px">Searchly</div>
  <div class="partner" style="left:720px"><i></i>Streamo</div>
  <div class="partner" style="left:911px"><i></i>Iconbay</div>
</section>

<!-- WHY CHOOSE -->
<section>
  <h2 class="sec-title center" style="top:846px">Why Choose <em>Us?</em></h2>
  <div class="rule" style="left:563px;top:884px;width:77px"></div>
  <p class="sec-sub" style="top:898px">Because ServLoom works for you.</p>

  <article class="why featured" style="left:189px">
    <h3>Free SSL Certificate</h3>
    <svg width="28" height="28" viewBox="0 0 28 28"><circle cx="14" cy="14" r="10" fill="#fff"/><circle cx="14" cy="14" r="4" fill="#1592e6"/><g stroke="#fff" stroke-width="3"><path d="M14 1v5M14 22v5M1 14h5M22 14h5"/></g></svg>
    <div class="dash"></div>
    <p>Let us put your website in front of consumers at the moment in time they are searching for your products &amp; services.</p>
  </article>
  <article class="why" style="left:483px">
    <h3>Managed Security</h3>
    <svg width="28" height="28" viewBox="0 0 28 28"><path d="M14 2 L25 6 V13 C25 20 20 25 14 27 C8 25 3 20 3 13 V6 Z" fill="#1592e6"/><path d="M14 6 L21 9 V13 C21 18 18 21 14 23 Z" fill="#fff"/></svg>
    <div class="dash"></div>
    <p>Let us put your website in front of consumers at the moment in time they are searching for your products &amp; services.</p>
  </article>
  <article class="why" style="left:778px">
    <h3>Customer Friendly</h3>
    <svg width="50" height="28" viewBox="0 0 50 28"><rect x="1" y="6" width="8" height="18" fill="#1592e6"/><rect x="41" y="6" width="8" height="18" fill="#1592e6"/><path d="M11 10 L22 6 L30 10 L39 10 V20 L28 26 L11 20 Z" fill="#1592e6"/><path d="M20 12 L28 10 L34 16" stroke="#fff" stroke-width="2" fill="none"/></svg>
    <div class="dash"></div>
    <p>Let us put your website in front of consumers at the moment in time they are searching for your products &amp; services.</p>
  </article>
</section>

<!-- FEATURES -->
<div class="blob" style="left:857px;top:1686px;width:366px;height:366px"></div>
<section class="abs band">
  <div class="abs" role="img" aria-label="Isometric illustration of server racks, a cloud and a laptop" style="left:150px;top:10px;width:297px;height:371px;border-radius:40px;background:linear-gradient(160deg,rgba(255,255,255,.35),rgba(210,225,245,.22))"></div>
  <h3 class="abs" style="left:622px;top:40px;font-size:18px;line-height:28px;font-weight:700;color:#fff">Best Features and Services<br>around the globe.</h3>

  <div class="tile" style="left:622px;top:133px"><svg width="40" height="40" viewBox="0 0 40 40" fill="none" stroke="#1f2a44" stroke-width="1.6"><circle cx="20" cy="18" r="9"/><circle cx="20" cy="18" r="3"/><path d="M20 5v4M20 27v4M7 18h4M29 18h4"/><path d="M8 36h24"/></svg><span>Fully Managed</span></div>
  <div class="tile" style="left:753px;top:133px"><svg width="40" height="40" viewBox="0 0 40 40" fill="none" stroke="#1f2a44" stroke-width="1.6"><rect x="12" y="4" width="16" height="10"/><rect x="6" y="22" width="12" height="12"/><rect x="22" y="22" width="12" height="12"/><path d="M20 14v4M12 18h16M12 18v4M28 18v4"/></svg><span>Free Migration</span></div>
  <div class="tile" style="left:884px;top:133px"><svg width="40" height="40" viewBox="0 0 40 40" fill="none" stroke="#1f2a44" stroke-width="1.6"><rect x="3" y="6" width="14" height="10"/><rect x="23" y="6" width="14" height="10"/><rect x="13" y="26" width="14" height="10"/><path d="M10 16v5h20v-5M20 21v5"/></svg><span>Multiple Devices</span></div>
  <div class="tile" style="left:622px;top:264px"><svg width="40" height="40" viewBox="0 0 40 40" fill="none" stroke="#1f2a44" stroke-width="1.6"><rect x="3" y="6" width="24" height="8"/><rect x="3" y="16" width="24" height="8"/><rect x="3" y="26" width="24" height="8"/><circle cx="31" cy="28" r="7"/><path d="M28 28l2 2 4-4"/></svg><span>Daily Backups</span></div>
  <div class="tile" style="left:753px;top:264px"><svg width="40" height="40" viewBox="0 0 40 40" fill="none" stroke="#1f2a44" stroke-width="1.6"><circle cx="20" cy="22" r="13"/><path d="M20 22l6-6M16 4h8M20 4v5"/></svg><span>Ultimate Speed</span></div>
  <div class="tile" style="left:884px;top:264px"><svg width="40" height="40" viewBox="0 0 40 40" fill="none" stroke="#1f2a44" stroke-width="1.6"><circle cx="20" cy="20" r="9"/><rect x="16" y="18" width="8" height="7"/><path d="M18 18v-3a2 2 0 0 1 4 0v3M20 3v6M20 31v6M3 20h6M31 20h6M8 8l4 4M28 28l4 4M32 8l-4 4M12 28l-4 4"/></svg><span>Best Security</span></div>
</section>

<!-- PRICING -->
<section>
  <h2 class="sec-title" style="left:466px;top:1792px">Hosting <em>Plans</em> &amp; <em>Pricings</em></h2>
  <div class="rule" style="left:466px;top:1830px;width:60px"></div>
  <p class="sec-sub" style="top:1846px">Premium quality is our top priority with good prices.</p>

  <article class="plan" style="left:189px">
    <div class="cap" style="background:linear-gradient(90deg,#1592e6,#1a7fd8)">PERSONAL</div>
    <div class="price">$10</div>
    <div class="tier">Limited Access</div>
    <ul><li><b></b>150 GB Disk Space</li><li><b></b>3 Sub Domains</li><li><b></b>5 Email Accounts</li><li><b class="no"></b>Daily Backup</li><li><b class="no"></b>License</li><li><b class="no"></b>Online Support</li></ul>
    <div class="buy" style="background:var(--blue)">Buy Now</div>
  </article>
  <article class="plan" style="left:472px">
    <div class="cap" style="background:linear-gradient(90deg,#ee6c14,#f08a1c)">BUSINESS</div>
    <div class="price">$30</div>
    <div class="tier">Limited Access</div>
    <ul><li><b></b>300 GB Disk Space</li><li><b></b>5 Sub Domains</li><li><b></b>7 Email Accounts</li><li><b></b>Daily Backup</li><li><b class="no"></b>License</li><li><b class="no"></b>Online Support</li></ul>
    <div class="buy" style="background:var(--orange)">Buy Now</div>
  </article>
  <article class="plan" style="left:757px">
    <div class="cap" style="background:linear-gradient(90deg,#fbb42a,#fcc33f)">ENTERPRISE</div>
    <div class="price">$50</div>
    <div class="tier">Unlimited Access</div>
    <ul><li><b></b>500 GB Disk Space</li><li><b></b>7Sub Domains</li><li><b></b>10 Email Accounts</li><li><b></b>Daily Backup</li><li><b></b>License</li><li><b></b>Online Support</li></ul>
    <div class="buy" style="background:var(--yellow)">Buy Now</div>
  </article>

  <p class="abs center" style="top:2355px;font-size:11.5px"><span style="text-decoration:underline;color:var(--navy)">See Plans and Pricing</span> for more information on latest features</p>
  <div class="btn btn-solid" style="left:507px;top:2391px;width:185px;height:30px;font-size:10px">View More Plans and Pricing</div>
</section>

<!-- GUARANTEE -->
<div class="blob" style="left:-77px;top:2678px;width:154px;height:154px"></div>
<section class="abs guarantee" role="img" aria-label="Blue-tinted photo of people working at laptops behind the guarantee message">
  <h2 class="abs center head" style="top:46px;font-size:20px;font-weight:800;color:#fff"><span style="color:#1ab3f0;font-weight:400">30 DAY</span> MONEY-BACK GUARANTEE</h2>
  <p class="abs center" style="top:84px;font-size:11px;color:rgba(255,255,255,.75)">Most flexible and affordable plans in whole industry</p>
  <div class="perk" style="left:366px;top:131px"><i></i>Easily upgrade or downgrade</div>
  <div class="perk" style="left:674px;top:131px"><i></i>Instant prorated refunds</div>
  <div class="perk" style="left:366px;top:177px"><i></i>2 months free if paid yearly</div>
  <div class="perk" style="left:674px;top:177px"><i></i>No fixed term contracts</div>
</section>

<!-- TESTIMONIALS -->
<section>
  <div class="ring" style="left:-330px;top:2860px;width:640px;height:640px"></div>
  <div class="ring" style="left:-230px;top:2960px;width:440px;height:440px"></div>
  <div class="ring" style="left:890px;top:2870px;width:640px;height:640px"></div>
  <div class="ring" style="left:990px;top:2970px;width:440px;height:440px"></div>

  <h2 class="sec-title" style="left:530px;top:2845px">Testimonials</h2>
  <div class="rule" style="left:530px;top:2888px;width:52px"></div>
  <p class="sec-sub" style="top:2907px">Be the part of our happy and satisfied clients</p>

  <div class="avatar" role="img" aria-label="Client portrait" style="left:152px;top:3004px"></div>
  <div class="avatar" role="img" aria-label="Client portrait" style="left:148px;top:3139px"></div>
  <div class="avatar" role="img" aria-label="Client portrait" style="left:254px;top:3316px"></div>
  <div class="avatar" role="img" aria-label="Client portrait" style="left:1090px;top:3027px"></div>
  <div class="avatar" role="img" aria-label="Client portrait" style="left:930px;top:3152px"></div>
  <div class="avatar" role="img" aria-label="Client portrait" style="left:902px;top:3321px"></div>

  <div class="abs quote-card">
    <p class="abs" style="left:43px;top:46px;width:350px;font-size:11px;line-height:17px;color:var(--text)">The best thing about ServLoom is their support and best services, they are always ready to be with us. And their plans are ordinary.</p>
    <div class="avatar" role="img" aria-label="Client portrait" style="left:43px;top:94px;width:54px;height:46px"></div>
    <p class="abs" style="left:115px;top:110px;font-size:10.5px;color:var(--navy)">Daniel Reyes</p>
    <p class="abs" style="left:115px;top:130px;font-size:10.5px;color:var(--blue)">CEO of Brightline Co</p>
  </div>
  <svg class="abs" style="left:427px;top:3034px" width="58" height="46" viewBox="0 0 58 46"><rect width="58" height="46" fill="#fff"/><rect x="8" y="2" width="42" height="42" fill="#1592e6"/><text x="29" y="36" text-anchor="middle" font-family="Merriweather Sans, sans-serif" font-weight="800" font-size="30" fill="#fff">“</text></svg>

  <svg class="abs" style="left:524px;top:3318px" width="150" height="18" viewBox="0 0 150 18" fill="none">
    <path d="M2 9h14M2 9l6-6M2 9l6 6" stroke="#1592e6" stroke-width="2"/>
    <circle cx="55" cy="9" r="6" fill="#1592e6"/>
    <circle cx="73" cy="9" r="5" stroke="#1592e6" stroke-width="1.5"/>
    <circle cx="89" cy="9" r="5" stroke="#1592e6" stroke-width="1.5"/>
    <path d="M146 9h-14M146 9l-6-6M146 9l-6 6" stroke="#1592e6" stroke-width="2"/>
  </svg>
</section>

<!-- BLOG -->
<section>
  <h2 class="sec-title center" style="top:3468px">Blog</h2>
  <p class="sec-sub" style="top:3525px">Get the latest news</p>
  <article class="post" style="left:189px">
    <div class="thumb" role="img" aria-label="Photo of two colleagues working together on a laptop" style="background:linear-gradient(150deg,#efe8df,#b8a590)"></div>
    <time>June 12, 2021</time>
    <h4>Aliquam nec libero at mauris dictum efficitur.</h4>
    <p>Lorem ipsum dolor sit amet, consectetur adipiscing elit. In purus urna, maximus eu consequat non, sollicitudin nec nisi.</p>
    <a>Read More →</a>
  </article>
  <article class="post" style="left:472px">
    <div class="thumb" role="img" aria-label="Photo of a modern meeting room with round lamps" style="background:linear-gradient(150deg,#d8dde3,#5d6a78)"></div>
    <time>June 12, 2021</time>
    <h4>Aliquam nec libero at mauris dictum efficitur.</h4>
    <p>Lorem ipsum dolor sit amet, consectetur adipiscing elit. In purus urna, maximus eu consequat non, sollicitudin nec nisi.</p>
    <a>Read More →</a>
  </article>
  <article class="post" style="left:757px">
    <div class="thumb" role="img" aria-label="Photo of a desk with a large monitor and shelves" style="background:linear-gradient(150deg,#e6e6e4,#3b3d42)"></div>
    <time>June 12, 2021</time>
    <h4>Aliquam nec libero at mauris dictum efficitur.</h4>
    <p>Lorem ipsum dolor sit amet, consectetur adipiscing elit. In purus urna, maximus eu consequat non, sollicitudin nec nisi.</p>
    <a>Read More →</a>
  </article>
</section>

<!-- CONTACT + FOOTER -->
<svg class="abs" style="left:0;top:4410px" width="1200" height="553" viewBox="0 0 1200 553">
  <defs>
    <linearGradient id="footBg" x1="0" y1="0" x2="0" y2="1">
      <stop offset="0" stop-color="#168fe3"/>
      <stop offset=".5" stop-color="#1a5fcb"/>
      <stop offset="1" stop-color="#1c3fb3"/>
    </linearGradient>
  </defs>
  <path d="M0 80 C300 60 800 10 1200 0 V553 H0 Z" fill="url(#footBg)"/>
</svg>

<section>
  <h2 class="sec-title" style="left:541px;top:4082px">Contact Us</h2>
  <div class="rule" style="left:541px;top:4121px;width:50px"></div>
  <p class="sec-sub" style="top:4137px">Get in touch with the best professional</p>

  <form class="abs form">
    <div class="field" style="left:63px;top:50px;width:438px"><label>FULL NAME</label></div>
    <div class="field" style="left:63px;top:114px;width:209px"><label>PERSONAL EMAIL</label></div>
    <div class="field" style="left:291px;top:114px;width:210px"><label>BUSINESS EMAIL</label></div>
    <div class="field" style="left:63px;top:178px;width:209px"><label>WEBSITE URL</label></div>
    <div class="field" style="left:291px;top:178px;width:210px"><label>PHONE NUMBER</label></div>
    <div class="field" style="left:63px;top:241px;width:438px"><label>WHAT CAN WE HELP YOU WITH?</label></div>
    <div class="btn btn-solid" style="left:212px;top:311px;width:127px;height:32px;font-size:10px">Submit</div>
  </form>
</section>

<footer class="foot">
  <div class="abs brand" style="left:545px;top:4662px;width:110px;height:30px;background:#fff;display:flex;align-items:center;justify-content:center;font-size:15px">SERVLOOM</div>

  <h4 style="left:189px;top:4726px">Quick Links</h4>
  <span style="left:189px;top:4760px">Home</span>
  <span style="left:189px;top:4785px">Domain</span>
  <span style="left:189px;top:4810px">Blog</span>
  <span style="left:189px;top:4835px">Plans</span>
  <span style="left:189px;top:4860px">Contact</span>

  <h4 style="left:530px;top:4729px">Social Links</h4>
  <a style="left:530px;top:4763px"><i></i>Friendwall</a>
  <a style="left:530px;top:4788px"><i></i>Snapgrid</a>
  <a style="left:530px;top:4813px"><i></i>Chirper</a>
  <a style="left:530px;top:4838px"><i></i>Workline</a>

  <h4 style="left:873px;top:4729px">Information</h4>
  <span style="left:873px;top:4763px"><svg width="11" height="11" viewBox="0 0 24 24"><path d="M6.6 10.8a15 15 0 0 0 6.6 6.6l2.2-2.2a1 1 0 0 1 1-.25 11.4 11.4 0 0 0 3.6.57 1 1 0 0 1 1 1V20a1 1 0 0 1-1 1A17 17 0 0 1 3 4a1 1 0 0 1 1-1h3.5a1 1 0 0 1 1 1c0 1.25.2 2.45.57 3.57a1 1 0 0 1-.25 1z" fill="#fff"/></svg>+1 800 555 0142</span>
  <span style="left:873px;top:4794px"><svg width="12" height="10" viewBox="0 0 24 18"><rect x="1" y="1" width="22" height="16" fill="none" stroke="#fff" stroke-width="2"/><path d="M1 1l11 9 11-9" fill="none" stroke="#fff" stroke-width="2"/></svg>hello@servloom.example</span>

  <span style="left:189px;top:4925px;font-size:10px;color:rgba(255,255,255,.55)">©ServLoom 2021 | All Rights Reserved</span>
  <span style="left:810px;top:4925px;width:186px;justify-content:flex-end;font-size:10px;color:rgba(255,255,255,.55)">Privacy Policy | Terms &amp; Conditions</span>
</footer>

</body>
</html>
```